KMR Info Brochure

We need a brochure design for a new not-for-profit organisation that is aimed at providing homeless people with a residence that also provides counselling and vocational training to assist them to find suitable employment at the end of the program.
PLEASE NOTE:
Brochure to be A4.
I know the brochure is quite long, it is really a booklet, but please note that it does not have to have a lot of work done on it, I just want it to look professional and the front cover and inside page to look good.
Also please leave about 2-3 pages at the end as I will be adding in some architect drawings.
Please add in a last page with Contact written at the bottom - we will fill that in later. So please ensure it is editable in PDF.
Thank you so much.
Cheers
Petra

```html
<!DOCTYPE html>
<html lang="en">
<head>
<meta charset="utf-8">
<title>KMR Info Brochure – Inner Pages Option 2</title>
<link href="https://fonts.googleapis.com/css2?family=Open+Sans:wght@400;600;700&display=swap" rel="stylesheet">
<style>
:root{
  --board:#3b3b3b;
  --label:#f2c200;
  --label-white:#ffffff;
  --paper:#ffffff;
  --olive:#a39e45;
  --olive-dark:#8c8738;
  --olive-light:#c8c38a;
  --ink:#555555;
  --ink-soft:#777777;
  --head:#6f6a22;
}
*{margin:0;padding:0;box-sizing:border-box}
html,body{width:877px;height:1200px;overflow:hidden;background:var(--board)}
body{position:relative;font-family:"Open Sans",Arial,sans-serif;color:var(--ink)}
.board-title{position:absolute;left:14px;top:9px;color:var(--label);font-size:15px;font-weight:700}
.page-label{position:absolute;color:var(--label-white);font-size:15px;font-weight:700}
.spread{position:absolute;left:80px;width:736px;display:flex;box-shadow:0 3px 12px rgba(0,0,0,.55)}
.spread.top{top:83px;height:501px}
.spread.bottom{top:627px;height:522px}
.page{position:relative;width:50%;height:100%;background:var(--paper);padding:32px 30px 0 27px;font-size:4.6px;line-height:6.6px;overflow:hidden}
.page.left{background:linear-gradient(to right,#fff 86%,#ebebeb 100%)}
.page.right{background:linear-gradient(to left,#fff 90%,#ebebeb 100%);padding-left:24px;padding-right:16px}
.section-bar{height:11px;margin-bottom:11px;background:linear-gradient(to right,var(--olive) 0%,var(--olive) 45%,rgba(163,158,69,0) 100%);color:#fff;font-weight:700;font-size:6.2px;line-height:11px;padding-left:7px;width:190px}
p{margin-bottom:7px}
h3{font-size:4.8px;font-weight:700;color:var(--head);margin:9px 0 6px}
.indent{padding-left:18px}
.ticks{display:grid;grid-template-columns:1fr 1fr;column-gap:10px;row-gap:2px;margin:5px 0 9px;padding-left:4px}
.ticks li{list-style:none;display:flex;align-items:center;gap:4px}
.tick{width:6px;height:6px;flex:none;background:var(--olive);border-radius:.6px;position:relative}
.tick::after{content:"";position:absolute;left:2px;top:.6px;width:1.7px;height:3.2px;border:solid #fff;border-width:0 .8px .8px 0;transform:rotate(45deg)}
.numbered li{list-style:none;display:flex;gap:12px;margin-bottom:6px;padding-left:4px}
.footnotes{position:absolute;left:24px;right:16px;font-size:3.5px;line-height:4.8px;color:var(--ink-soft)}
.footer{position:absolute;bottom:8px;height:10px;display:flex;align-items:center;gap:6px}
.page.left .footer{left:22px;right:0}
.page.right .footer{left:0;right:22px;flex-direction:row-reverse}
.folio{font-size:5.5px;color:var(--ink-soft)}
.brand{font-size:5.5px;font-weight:700;color:var(--olive-dark)}
.footer-band{flex:1;height:8px;background:var(--olive-light)}
</style>
</head>
<body>

<div class="board-title">Inner page Option - 2</div>
<div class="page-label" style="left:83px;top:52px">Page 4</div>
<div class="page-label" style="left:756px;top:52px">Page 5</div>
<div class="page-label" style="left:83px;top:1160px">Page 6</div>
<div class="page-label" style="left:756px;top:1160px">Page 7</div>

<section class="spread top">
  <article class="page left">
    <div class="section-bar">Executive Summary</div>
    <p>KMR Legacy Foundation (KMR) is a not-for-profit organisation that will attempt to break the cycle of homelessness. KMR will provide a live-in residence for people from all age groups and provide psychological counselling to address the issues associated with the causes, effects, and impact of homelessness.</p>
    <p>It is expected that most Residents will require an average twelve months in residence to address their psychological issues; during this time the Resident will also be provided with various types of training, from life skills to specific vocational education, to assist them to move towards independent living.</p>
    <p>Once the Resident is ready, KMR staff will assist the Resident with all aspects of transitioning to independent living and provide on-going assistance and support for as long as is required.</p>
    <p>KMR will cater for family groups and single parents, providing counselling for the entire family group and training for the parent. During the residency the children will attend a local school to reduce the impact to their education.</p>
    <p>KMR recognises that the cost of running the facility and providing long and work experience to a reasonably large group of people in today's economic environment will be challenging. As such, KMR is seeking funding for the initial establishment of the facility, but aims to introduce a number of separate complementary business entities that will provide the necessary training avenue and income required for the aim of eventually being self-sustaining.</p>
    <p>Overall, KMR aims to reduce the overall incidence of homelessness in Australia wide.</p>
    <p style="margin-top:18px">Residents = homeless people living at KMR complex</p>
    <p>Clients = Residents who have been through the Program and returned to independent living, but remain in the After Care program</p>
    <footer class="footer">
      <span class="folio">4</span>
      <span class="brand">KMR</span>
      <span class="footer-band"></span>
    </footer>
  </article>

  <article class="page right">
    <div class="section-bar">1. Homelessness</div>
    <p>Numerous national, state and local reports repeatedly indicate that there is not one single cause that leads to homelessness. However without the financial ability to make ends meet and afford a home, individuals and families become homeless. Other factors that contribute to homelessness include:</p>
    <ul class="ticks">
      <li><span class="tick"></span>Poverty</li>
      <li><span class="tick"></span>Unemployment</li>
      <li><span class="tick"></span>Lack of affordable housing</li>
      <li><span class="tick"></span>Poor physical or mental health</li>
      <li><span class="tick"></span>Drug and alcohol abuse</li>
      <li><span class="tick"></span>Gambling</li>
      <li><span class="tick"></span>Family and relationship breakdown</li>
      <li><span class="tick"></span>Domestic violence</li>
      <li><span class="tick"></span>Physical and/or sexual abuse</li>
    </ul>
    <p>There are currently 105,237 people in Australia who are homeless. The rate of homelessness is 49 out of every 10,000 people (0.5% of the population). There are approximately 56% male and 44% female. The age breakdown is as follows:</p>
    <ul class="ticks">
      <li><span class="tick"></span>Under 12 17% (17,845)</li>
      <li><span class="tick"></span>12–18 10% (10,513)</li>
      <li><span class="tick"></span>19–24 15% (15,325)</li>
      <li><span class="tick"></span>25–34 19% (19,312)</li>
      <li><span class="tick"></span>35–44 14% (14,494)</li>
      <li><span class="tick"></span>45–54 12% (12,537)</li>
      <li><span class="tick"></span>55–64 9% (8,940)</li>
      <li><span class="tick"></span>65–74 4% (4,774)</li>
      <li><span class="tick"></span>75 and over 2% (2,008)</li>
    </ul>
    <p>Due to the wide spread of demographics of homeless people, KMR will cater for all age ranges and sexes, as well as family groups. The target market for KMR will be anyone that is homeless, 'sleeping rough' or 'couch surfing'. Secondary placement consideration will also be given to anyone else on a case-by-case basis. The current homeless statistics are as follows:</p>
    <ul class="ticks">
      <li><span class="tick"></span>NSW 28,190 (40.8 people per 10,000)</li>
      <li><span class="tick"></span>VIC 22,789 (42 people per 10,000)</li>
      <li><span class="tick"></span>QLD 19,838 (45 people per 10,000)</li>
      <li><span class="tick"></span>SA 5,985 (37.5 people per 10,000)</li>
      <li><span class="tick"></span>WA 9,592 (42.8 people per 10,000)</li>
      <li><span class="tick"></span>TAS 1,579 (31.9 people per 10,000)</li>
      <li><span class="tick"></span>NT 15,479 (730.7 people per 10,000)</li>
      <li><span class="tick"></span>ACT 1,785 (50 people per 10,000)</li>
    </ul>
    <div class="footnotes" style="top:426px">
      <p style="margin-bottom:3px">¹ http://www.shelterfacts.example/what-drives-homelessness/key-causes-and-figures</p>
      <p style="margin-bottom:3px">² http://www.housingdata.example/national/homelessness-statistics</p>
      <p>³ The number of people sleeping in the house with reported figures from the latest national survey are at a rate per ten thousand, drawn from official census records.</p>
    </div>
    <footer class="footer">
      <span class="folio">5</span>
      <span class="brand">KMR</span>
      <span class="footer-band"></span>
    </footer>
  </article>
</section>

<section class="spread bottom">
  <article class="page left">
    <div class="section-bar">2. Program Overview</div>
    <p>KMR Legacy Foundation (KMR) aims to provide homeless people (Residents) with the tools necessary to re-enter society as functional, productive and balanced members of society. KMR aims to assist homeless people, not by just giving them a shelter, but by addressing the initial cause of homelessness and provide the tools necessary to gain independent living, in an one stop the cycle.</p>
    <p>KMR will house Residents in a residential facility while they are at the facility they will receive physiological and psychological care, assistance with basic society life skills and/or vocational skills and training. Once the Residents have completed their program, KMR will assist them to fit back into society, find a job (if relevant), appropriate housing, schooling etc. KMR will continue to provide Residents with Outreach and After Care assistance for as long as required.</p>
    <h3>2.1. &nbsp;Physiological</h3>
    <p class="indent">Due to poor diet, malnutrition and exposure, homeless people are at greater risk of suffering from chronic health disorders like asthma, hepatitis and diabetes. Furthermore, many homeless adolescents find that exchanging sex for food, clothing, and shelter is their only chance of survival on the streets. Reportedly, one in four youths have traded sex for survival, which means they are at greater risk of contracting AIDS, HIV-related illnesses, and other STDs.</p>
    <p class="indent">In addition, older homeless people may suffer significant dental lapses and ophthalmological disorders that go untreated for significant periods of time.</p>
    <p class="indent">As part of the intake process, KMR will do a complete medical assessment of each Resident to assess their level of wellness. A program of treatment will be initiated in accordance with the results of the medical and dental assessment.</p>
    <h3>2.2. &nbsp;Psychological</h3>
    <p class="indent">A majority of Residents will experience some form of anxiety disorders, depression, post-traumatic stress disorder and suicidal thoughts due to the increased exposure to violence while homeless. Therefore, it will be a requirement for all Residents to undertake counselling sessions throughout their stay at the KMR facility.</p>
    <p class="indent">At the initial intake process a full psychological analysis will be undertaken and a specific program will be developed for each Resident. Regular counselling sessions (and any other treatment necessary) will be conducted to address each Resident's issues with the aim of addressing the cause/impact of homelessness.</p>
    <h3>2.3. &nbsp;Learning/Training</h3>
    <p class="indent">Life skills are the skills that many people have for granted, like managing money, shopping, cooking and security requirements (eg voting, paying taxes etc). These skills are essential for living independently. Some homeless people do not have all of these skills, either because they never acquired them or because they lost them through extended periods of homelessness. Helping homeless people acquire life skills can help them move on from homelessness and resettle into the community. Life skills training is different from support, help or assistance in that the aim is to promote self-sufficiency.</p>
    <p class="indent">Life skills can be thought of in terms of four broad categories:</p>
    <ul class="numbered indent">
      <li><span>1)</span><span>Core or basic skills (eg. numeracy, literacy and information technology)</span></li>
      <li><span>2)</span><span>Independent living skills (eg. finance, nutrition, employment)</span></li>
    </ul>
    <footer class="footer">
      <span class="folio">6</span>
      <span class="brand">KMR</span>
      <span class="footer-band"></span>
    </footer>
  </article>

  <article class="page right">
    <ul class="numbered indent" style="margin-top:2px">
      <li><span>3)</span><span>Social skills (eg. interpersonal skills, conflict resolution, developing self-confidence and social networks)</span></li>
      <li><span>4)</span><span>Society Requirements (eg. voting, taxation etc)</span></li>
    </ul>
    <p>It is anticipated that most Residents will need to undertake some aspect of Life Skills, which skills are required will be assessed during the initial intake phase. Life Skills content will vary widely depending upon the individual requirement.</p>
    <h3>2.4. &nbsp;Special Needs</h3>
    <p class="indent">According to one study, the number of homeless youth diagnosed with learning disabilities is double the rate of other children. Another study found that 38% of homeless youth have ADD. As such, KMR plans to work one on one with Residents with learning disabilities to assist them to undertake various training options with the final aim of placing them in a suitable employment situation.</p>
    <h3>2.5. &nbsp;Vocational Education</h3>
    <p class="indent">Vocational education is education that prepares people for specific trades, crafts and careers at various levels from a trade, a craft, technician, or a professional position. Residents will work closely with their Case Manager and decide on a way forward for the individual, based on their skills, abilities, likes and dislikes, attitude and aptitude. Appropriate training will be sourced to suit the Residents individual needs and a plan to help the individual Resident towards his/her goals will be developed.</p>
    <p class="indent">KMR will do everything in its power to assist the Resident to achieve their desired outcomes, as vocational skills training is the cornerstone of Residents moving into independent living options.</p>
    <h3>2.6. &nbsp;Fitting back into Society</h3>
    <p class="indent">Once the Residents are ready to fit back into Society, KMR will assist them every step of the way. The Residents Caseworker will help them through all aspects of independent living assisting them with finding:</p>
    <ul class="ticks indent">
      <li><span class="tick"></span>Appropriate Employment</li>
      <li><span class="tick"></span>Housing / tenancy agreements</li>
      <li><span class="tick"></span>Connecting utilities</li>
      <li><span class="tick"></span>Furnishing</li>
      <li><span class="tick"></span>Transportation</li>
      <li><span class="tick"></span>Schools</li>
      <li><span class="tick"></span>Churches</li>
      <li><span class="tick"></span>Clubs/meeting locations</li>
    </ul>
    <h3>2.7. &nbsp;Outreach / After Care Program</h3>
    <p class="indent">Once a Resident has finished the internal program, they will be transitioned over a period of time to become a Client. The Client will be assisted to fit back into society (see above) over a period of time to ensure that they have every chance of success.</p>
    <div class="footnotes" style="top:436px">
      <p>⁴ Source for Children, Youth and Families, Centre for Social Outcomes Studies, Reconnecting Young Homeless and Runaway Youth, Civic Wellbeing Institute Report on Learning Needs.</p>
    </div>
    <footer class="footer">
      <span class="folio">7</span>
      <span class="brand">KMR</span>
      <span class="footer-band"></span>
    </footer>
  </article>
</section>

</body>
</html>
```